Independent Midwife for a positive birth experience needs a vibrant, and elegant business card/logo

I need a business card design with a logo. The logo I would like to be able to use on my website (www.midwifeorlaith.com) next to my name.
Therefore the design of the card and logo should suit the colours and design of the website. The title of the website and company is "Orlaith Denby Marsworth, Midwife" but I'd like to have the business card title to be "Orlaith Denby Marsworth - Independent Midwife" in bold letters, same script font as in my website.

I provide gold standard midwifery services, one-to-one tailored care, continuity of care throughout the entire pregnancy (antenatal care), the birth and after the birth (postnatal care), home birth, water birth, breast-feeding support, and birth preparation workshops. I also am certified and offer complementary therapies: pregnancy reflexology, rebozo techniques for optimal baby positioning.

The design should incorporate similar colours and style as the website and the "Orlaith Denby Marsworth - Independent Midwife" on the card should include the same font as in the title of the website, however, in bold. The front of the card should have a logo, title and contact information (phone number 071592604, email orlaith.marsworth@quillpost.com, website address www.midwifeorlaith.com).
The back of the card to include the services I offer.

The logo: use of colour purple (varying shades), should communicate communicate warmth, kindness, compassion. It should convey that I'm a midwife who believes in fostering a trusting relationship with my clients and to provide them with a positive pregnancy and birth experience.

Target Market(s)

Pregnant women or women who are looking to book a private midwife for better birth experience and outcome

Industry/Entity Type

Baby

Contact Information for Business Card

Name and Title on front side together with contact details
The reverse side should have services/packages offered

Font styles to use
Script
Other font styles liked:
• similar script as in my website for name and title, and easy to read font for the rest of the words

Colors
b768aa
a54599
d2a4cc
ffffff

Requirements
Must have
• same font as title of website, but slightly bolder.
• similar design, colours, patterns as in website.
• Also include a gold accent colour somewhere in the design please.
Nice to have
• perhaps a logo of pregnant belly in profile or newborn baby icon

```html
<!DOCTYPE html>
<html lang="en">
<head>
<meta charset="utf-8">
<title>Orlaith Denby Marsworth - Independent Midwife</title>
<link rel="stylesheet" href="https://fonts.googleapis.com/css2?family=Tangerine:wght@700&family=Open+Sans:ital,wght@1,600&display=swap">
<style>
  :root {
    --violet: #9a1ff0;
    --violet-soft: #d2a4cc;
    --lavender-mist: #efe4f6;
    --figure-line: #c9a6ec;
    --gold: #e8ec3a;
    --paper: #ffffff;
  }
  html, body {
    margin: 0;
    padding: 0;
    overflow: hidden;
    background: var(--paper);
  }
  .card {
    position: relative;
    width: 1200px;
    height: 702px;
    background: var(--paper);
    overflow: hidden;
  }
  .leaf-motif {
    position: absolute;
    left: 640px;
    top: 378px;
    width: 528px;
    height: 278px;
    background: radial-gradient(ellipse at 60% 45%, var(--lavender-mist) 0%, rgba(239,228,246,0.55) 45%, rgba(255,255,255,0) 75%);
  }
  .mother-figure {
    position: absolute;
    left: 556px;
    top: 142px;
    width: 88px;
    height: 180px;
    border-radius: 44px 44px 30px 30px;
    background: linear-gradient(180deg, rgba(201,166,236,0.35) 0%, rgba(201,166,236,0.22) 70%, rgba(232,236,58,0.45) 82%, rgba(201,166,236,0.15) 100%);
  }
  .title {
    position: absolute;
    left: 0;
    top: 0;
    width: 1200px;
    height: 702px;
  }
  .title-text {
    font-family: "Tangerine", cursive;
    font-weight: 700;
    font-size: 84px;
    fill: var(--violet);
  }
  .title-rule {
    stroke: var(--violet);
    stroke-width: 3.5;
  }
  .contact {
    position: absolute;
    right: 64px;
    top: 512px;
    margin: 0;
    text-align: right;
    font-family: "Open Sans", sans-serif;
    font-style: italic;
    font-weight: 600;
    font-size: 22px;
    letter-spacing: 2.2px;
    color: var(--violet);
    line-height: 41px;
  }
  .contact-line {
    display: block;
  }
</style>
</head>
<body>
  <main class="card">
    <div class="leaf-motif" role="img" aria-label="Faint lavender leaf ornament"></div>
    <div class="mother-figure" role="img" aria-label="Line illustration of a pregnant woman in profile with a gold accent at the belly"></div>

    <svg class="title" viewBox="0 0 1200 702" aria-labelledby="card-title">
      <text id="card-title" class="title-text" x="169" y="350" textLength="837" lengthAdjust="spacingAndGlyphs">Orlaith Denby Marsworth - Independent Midwife</text>
      <line class="title-rule" x1="169" y1="366" x2="1006" y2="366"/>
    </svg>

    <p class="contact">
      <span class="contact-line">Contact Number : +44-71592604</span>
      <span class="contact-line">Email : orlaith.marsworth@quillpost.com</span>
      <span class="contact-line">Visit : www.midwifeorlaith.com</span>
    </p>
  </main>
</body>
</html>
```